Real Estate - Large Sign Design

I am looking for a fresh new look for our leasing signs that will be showcase in front of commercial buildings available for lease. The sign dimension can be either 8'x4' or 4'x8'. They must exemplify our brand (see attachments) and be very visible by people driving by at high speeds.
They must include the following:
- Our logo (vector attached)
- Office Space Available
- 482-917-3064
- Mara Finch
- Peter Vale
- www.lorvanix.com
Please let me know if you have any questions.
Target Market(s)
Drivers in high traffic areas, walking crowds
Industry/Entity Type
Real Estate
Requirements
Must have
- They must include the following:
- - Our logo (vector attached)
- - Office Space Available
- - 482-917-3064
- - Mara Finch
- - Peter Vale
- - www.lorvanix.com
Should not have
- Should not be busy or hard to read.

```html
<!DOCTYPE html>
<html lang="en">
<head>
<meta charset="utf-8">
<title>Office Space Available – Leasing Signs</title>
<link href="https://fonts.googleapis.com/css2?family=Roboto+Condensed:ital,wght@0,400;0,700;1,400;1,700&display=swap" rel="stylesheet">
<style>
  :root {
    --bg-top: #7d7d7d;
    --bg-bottom: #2e2e2e;
    --sign-white: #ffffff;
    --ink: #111814;
    --ink-green: #2f6e5a;
    --slate-green: #3f5e58;
    --brand-green: #12a356;
    --lime: #c4d65a;
    --slate: #4b5868;
  }
  * { margin: 0; padding: 0; box-sizing: border-box; }
  html, body { width: 1200px; height: 1000px; overflow: hidden; }
  body {
    position: relative;
    background: linear-gradient(to bottom, var(--bg-top), var(--bg-bottom) 60%);
    font-family: "Roboto Condensed", "Arial Narrow", sans-serif;
  }
  .sign { position: absolute; background: var(--sign-white); overflow: hidden; }
  .sign-portrait { left: 79px; top: 213px; width: 343px; height: 685px; }
  .sign-landscape { left: 471px; top: 556px; width: 686px; height: 342px; }
  .sign-art { position: absolute; inset: 0; width: 100%; height: 100%; }
  .sign-text { position: absolute; line-height: 1; white-space: nowrap; }
  .headline { font-weight: 700; color: var(--ink); letter-spacing: -2px; }
  .subhead { font-weight: 400; color: var(--ink-green); letter-spacing: 1px; }
  .contact-name { font-weight: 700; color: var(--slate-green); }
  .contact-phone { font-weight: 700; color: #000; letter-spacing: -0.5px; }
  .contact-web { font-style: italic; color: #111; }
  .cta-tag {
    position: absolute; left: 23px; top: 399px; width: 155px; height: 25px;
    background: var(--brand-green); color: #fff;
    font-style: italic; font-weight: 700; font-size: 17px; line-height: 25px;
    padding-left: 7px;
  }
  .cta-tag::after {
    content: ""; position: absolute; right: 0; bottom: -10px;
    border-left: 10px solid transparent; border-top: 10px solid var(--brand-green);
  }
  .brand-name {
    position: absolute; color: #fff; font-weight: 400; font-size: 19px;
    line-height: 1; text-align: right; text-transform: uppercase; letter-spacing: 0.5px;
  }
</style>
</head>
<body>

<section class="sign sign-portrait">
  <svg class="sign-art" viewBox="0 0 343 685" aria-hidden="true">
    <defs>
      <linearGradient id="portraitWedge" x1="0" y1="0" x2="0" y2="1">
        <stop offset="0" stop-color="#c9d95c"/>
        <stop offset="0.5" stop-color="#7cc26a"/>
        <stop offset="1" stop-color="#3dbb72"/>
      </linearGradient>
      <linearGradient id="portraitBand" x1="0" y1="0" x2="1" y2="0">
        <stop offset="0" stop-color="#4b5868"/>
        <stop offset="0.45" stop-color="#2f7a5e"/>
        <stop offset="1" stop-color="#12a356"/>
      </linearGradient>
    </defs>
    <polygon points="343,0 343,600 258,600" fill="url(#portraitWedge)"/>
    <polygon points="0,662 343,540 343,685 0,685" fill="url(#portraitBand)"/>
  </svg>
  <div class="sign-text headline" style="left:20px;top:36px;font-size:96px;">OFFICE</div>
  <div class="sign-text headline" style="left:20px;top:120px;font-size:96px;">SPACE</div>
  <div class="sign-text subhead" style="left:21px;top:213px;font-size:56px;">AVAILABLE</div>
  <div class="cta-tag">Contact us Now!</div>
  <div class="sign-text contact-name" style="left:24px;top:440px;font-size:25px;">Peter Vale</div>
  <div class="sign-text contact-phone" style="left:22px;top:470px;font-size:38px;">482-917-30</div>
  <div class="sign-text contact-web" style="left:24px;top:513px;font-size:21px;">www.lorvanix.com</div>
  <div class="brand-name" style="right:6px;top:605px;">Hollis<br>Realty<br>Group</div>
</section>

<section class="sign sign-landscape">
  <svg class="sign-art" viewBox="0 0 686 342" aria-hidden="true">
    <defs>
      <linearGradient id="landscapeWedge" x1="0" y1="0" x2="0" y2="1">
        <stop offset="0" stop-color="#4b5868"/>
        <stop offset="0.5" stop-color="#2e8a60"/>
        <stop offset="1" stop-color="#12a356"/>
      </linearGradient>
      <linearGradient id="landscapeBand" x1="0" y1="0" x2="1" y2="0">
        <stop offset="0" stop-color="#c4d65a"/>
        <stop offset="0.6" stop-color="#6cc16c"/>
        <stop offset="1" stop-color="#3bb86e"/>
      </linearGradient>
    </defs>
    <polygon points="0,338 686,238 686,342 0,342" fill="url(#landscapeBand)"/>
    <polygon points="686,0 686,342 530,342" fill="url(#landscapeWedge)"/>
  </svg>
  <div class="sign-text headline" style="left:24px;top:22px;font-size:92px;">OFFICE SPACE</div>
  <div class="sign-text subhead" style="left:25px;top:108px;font-size:70px;color:#2f7d62;">AVAILABLE</div>
  <div class="sign-text contact-name" style="left:25px;top:203px;font-size:28px;">PETER VALE</div>
  <div class="sign-text contact-phone" style="left:23px;top:229px;font-size:50px;">482-917-3064</div>
  <div class="sign-text contact-web" style="left:25px;top:277px;font-size:21px;">www.lorvanix.com</div>
  <div class="brand-name" style="right:14px;top:268px;">Hollis<br>Realty<br>Group</div>
</section>

</body>
</html>
```